M&A Advisory firm needs elegant and powerful letterhead

We need a powerful but elegant letterhead to engage with the international financial industry.

Target Market(s)

New York and International Financial Industry

Industry/Entity Type

Finance

Font styles to use
Other font styles liked:
• Poppins

Requirements
Must have
• 482 W 71st Street 14th Floor New York, NY 10157 O: +1 (212) 555 0147 F: +1 (212) 555 0182

```html
<!DOCTYPE html>
<html lang="en">
<head>
<meta charset="utf-8">
<title>Meridane Letterhead</title>
<link rel="stylesheet" href="https://fonts.googleapis.com/css2?family=Poppins:wght@300;400&family=Open+Sans:wght@400&display=swap">
<style>
  :root {
    --brand-blue: #0d5394;
    --text-gray: #8a8a8a;
    --backdrop: #c8c8c8;
    --paper: #ffffff;
  }
  * { margin: 0; padding: 0; box-sizing: border-box; }
  html, body {
    width: 1200px;
    height: 878px;
    overflow: hidden;
    background: var(--backdrop);
  }
  .letterhead {
    position: absolute;
    left: 289px;
    top: 0;
    width: 621px;
    height: 878px;
    background: var(--paper);
    font-family: "Open Sans", sans-serif;
  }
  .brand {
    position: absolute;
    left: 52px;
    top: 78px;
    display: flex;
    align-items: center;
    gap: 10px;
  }
  .brand-dot {
    width: 18px;
    height: 18px;
    border-radius: 50%;
    background: var(--brand-blue);
  }
  .brand-name {
    font-family: "Poppins", sans-serif;
    font-weight: 300;
    font-size: 38px;
    letter-spacing: 1px;
    color: var(--brand-blue);
    line-height: 1;
  }
  .header-divider {
    position: absolute;
    left: 322px;
    top: 58px;
    width: 1px;
    height: 78px;
    background: var(--brand-blue);
  }
  .contact {
    position: absolute;
    left: 338px;
    top: 60px;
    font-family: "Poppins", sans-serif;
    font-weight: 300;
    font-size: 11.5px;
    line-height: 1.5;
    color: var(--brand-blue);
    letter-spacing: 0.4px;
  }
  .contact .address { margin-top: 8px; }
  .letter-body {
    position: absolute;
    left: 70px;
    top: 250px;
    width: 480px;
    font-size: 9.5px;
    line-height: 2;
    color: var(--text-gray);
  }
  .salutation { margin-bottom: 22px; }
  .letter-body p + p { margin-top: 14px; }
  .signature {
    position: absolute;
    left: 70px;
    top: 640px;
    font-size: 9.5px;
    line-height: 2.2;
    color: var(--text-gray);
  }
  .footer-rule {
    position: absolute;
    left: 150px;
    top: 778px;
    width: 430px;
    height: 1px;
    background: var(--brand-blue);
  }
  .footer-band {
    position: absolute;
    left: 168px;
    top: 796px;
    width: 453px;
    height: 22px;
    background: var(--brand-blue);
  }
  .footer-block {
    position: absolute;
    left: 0;
    top: 836px;
    width: 34px;
    height: 20px;
    background: var(--brand-blue);
  }
  .footer-brand {
    position: absolute;
    left: 48px;
    top: 798px;
    font-family: "Poppins", sans-serif;
    font-weight: 300;
    font-size: 15px;
    letter-spacing: 0.5px;
    color: var(--brand-blue);
  }
</style>
</head>
<body>
  <main class="letterhead">
    <header>
      <div class="brand">
        <span class="brand-dot"></span>
        <span class="brand-name">MERIDANE</span>
      </div>
      <div class="header-divider"></div>
      <address class="contact" style="font-style:normal">
        <div>O: +1 (212) 555 0147</div>
        <div>F: +1 (212) 555 0182</div>
        <div class="address">482 W 71st Street 14th Floor<br>New York, NY 10157</div>
      </address>
    </header>

    <section class="letter-body">
      <p class="salutation">Dear Ms. Laurent,</p>
      <p>We appreciate the opportunity to present our advisory services for your proposed transaction. Our team has reviewed the materials shared last week and prepared an initial view of value, timing and likely buyer interest across domestic and international markets.</p>
      <p>In the coming weeks we will refine the financial model, confirm key assumptions with your management and outline a clear process for outreach. We look forward to discussing next steps at your earliest convenience.</p>
    </section>

    <section class="signature">
      <div>Daniel Hart</div>
      <div>Co-Founder &amp; CEO</div>
    </section>

    <footer>
      <div class="footer-rule"></div>
      <div class="footer-brand">MERIDANE</div>
      <div class="footer-band"></div>
      <div class="footer-block"></div>
    </footer>
  </main>
</body>
</html>
```